Product page for a RV Motorsim Simulator

I want a look and feel similar to this link.
https://brovadaseats.com/products/q-zx-mini-lapforge-edition/
With the following text...
Get a Sim Racing Rig…
…That Saves Money & Performs Like an Ace

Take Your Sim Racing to the Next Level
The new RV Motorsim Pro Rig is all about delivering a top-notch sim racing experience. This home racing cockpit’s design is inspired with the vision to look minimal and yet offer everything that any starting up or amateur simulation racer would love to have in their rig. To serve the needs of more serious sim racing gamers, we designed the RV Motorsim Pro Rig frame around the world’s most celebrated sim racer Marek Olsvind’s own preferences.
Set up your rig, install your hardware and games, sit in your seat, and lose yourself in the authentic sim racing experience delivered with a true racing posture and controls placement that pro track racers enjoy.
Set Your Rig Up to Fit Your Needs
Meeting the needs of the modern home sim racing gamers, the RV Motorsim Pro Rig is designed to offer a lot of adjustment. Without compromising on the authentic race driving position, you can adjust most components of the rig so you can have just the kind of sim racing experience you like. This professional grade sim racing cockpit comes with adjustable settings for the seat, steering wheel, pedal plate, shifter and handbrake support, among other tweakable functions.
Enjoy the Best of Performance and Pricing
The RV Motorsim Pro Rig gives you optimal performance with a commercial grade build and a simpler, compatible frame design that will conveniently turn your home into your favorite virtual race track. More than that, we have ensured you get the best product at a price few others are offering and none with the features and functions integrated into the RV Motorsim Pro Rig.
With this perfect blend of performance, endurance, design, and price, you have no reason to go look for other sim racing rigs.
A Compatible Companion
The RV Motorsim Pro Rig is built to serve you. Whatever your preferences in console and controllers be, you will find this sim racing rig fully compatible with all the popular products available in the market.

STURDY BUILD QUALITY

This MarekOlsvind inspired sim racing rig is built with durable aluminum to give you a cockpit you can sit and race away for years to come. It is built to endure and deliver.

ADJUSTABLE COMPONENTS

Set your rig components to fit your space requirements and personal posture preferences. From steering wheel position and seat-screen distance to your pedal plate and more, you can adjust every such part to get the best racing experience.
A COMPLETE PACKAGE

Your RV Motorsim Pro Rig comes as a complete package. The box contains a pre-installed base, wheel mount, side mount, wheel mount support, and seat bracket.

Perfection Reimagined
With the RV Motorsim Pro Rig, you get the best value out of your money. At the same time, you are making sure your sim racing experience will be more fulfilling, exciting and comfortable than before.
Do You Want to be the Next MarekOlsvind?
We have put together the best in design, durability and performance for you. It’s time you took your sim racing passion to the next level.
Feel inspired and get the rig that will give you 100% satisfaction. Order today.

Target Market(s)

Online esport racing fans

Industry/Entity Type

Gaming

Number of Pages Required

1 page

Requirements
Must have
• racing related graphic designs

```html
<!DOCTYPE html>
<html lang="en">
<head>
<meta charset="utf-8">
<title>RV Motorsim Pro Rig</title>
<link href="https://fonts.googleapis.com/css2?family=Exo+2:wght@600;700;800;900&family=Roboto:wght@400;500;700&display=swap" rel="stylesheet">
<style>
:root{
  --bg:#0b0b0e;
  --bg-soft:#111216;
  --blue:#1d55e0;
  --blue-deep:#0d2a8a;
  --orange:#f07f1c;
  --white:#ffffff;
  --muted:#b9bcc6;
  --footer:#08080a;
}
*{margin:0;padding:0;box-sizing:border-box}
html,body{width:1200px;height:4232px;overflow:hidden;background:var(--bg)}
body{position:relative;font-family:"Roboto",sans-serif;color:var(--white)}
.abs{position:absolute}
.heading{font-family:"Exo 2",sans-serif;font-weight:800;text-transform:uppercase;line-height:1.08;font-size:38px;letter-spacing:.5px}
.heading .blue{color:var(--blue)}
.heading .orange{color:var(--orange)}
.body-text{font-size:12.5px;line-height:1.55;color:var(--muted)}
.accent{position:absolute;height:3px;width:60px;background:var(--orange)}

/* hero */
.hero{left:0;top:0;width:1200px;height:690px;background:
  radial-gradient(ellipse at 70% 40%,rgba(80,140,255,.55),transparent 55%),
  radial-gradient(ellipse at 20% 60%,rgba(40,90,230,.5),transparent 60%),
  linear-gradient(180deg,#0f2f9a 0%,#1745c9 45%,#0b2166 100%)}
.hero-shade{left:0;top:0;width:1200px;height:690px;background:rgba(5,15,60,.35)}
.logo{left:120px;top:50px;font-family:"Exo 2",sans-serif;font-weight:800;font-size:30px;letter-spacing:.5px;color:var(--white)}
.lang{left:930px;top:52px;width:44px;height:24px;border:1px solid rgba(255,255,255,.7);font-size:11px;display:flex;align-items:center;justify-content:center;gap:4px}
.lang i{display:inline-block;width:12px;height:8px;background:#c33}
.menu{left:1010px;top:52px;width:30px}
.menu span{display:block;height:4px;background:var(--white);margin-bottom:6px;border-radius:2px}
.hero-title{left:0;top:226px;width:1200px;text-align:center;font-family:"Exo 2",sans-serif;font-weight:900;font-size:62px;text-transform:uppercase;letter-spacing:1px}
.hero-sub{left:0;top:318px;width:1200px;text-align:center;font-family:"Exo 2",sans-serif;font-weight:700;font-size:26px}
.cta{left:484px;top:412px;width:232px;height:68px;border-radius:34px;background:var(--orange);font-family:"Exo 2",sans-serif;font-weight:800;font-size:18px;text-transform:uppercase;display:flex;align-items:center;justify-content:center;letter-spacing:.5px}
.slide-count{left:1106px;top:182px;font-family:"Exo 2",sans-serif;font-weight:800;font-size:30px}
.dots{left:1122px;top:250px;width:8px}
.dots span{display:block;width:8px;height:8px;border-radius:50%;background:var(--white);margin-bottom:22px}
.mouse{left:586px;top:588px}

/* photos */
.photo-frame{position:absolute;clip-path:polygon(8% 0,100% 0,92% 100%,0 100%);background:var(--white);padding:10px}
.photo{width:100%;height:100%;clip-path:polygon(8% 0,100% 0,92% 100%,0 100%)}
.photo-white{background:linear-gradient(135deg,#ffffff 0%,#dfe3ea 55%,#bfc6d2 100%)}
.photo-track{background:linear-gradient(160deg,#3a3f48 0%,#6b7280 40%,#1d55e0 75%,#11141b 100%)}

.sec1-photo{left:170px;top:730px;width:400px;height:300px}
.sec2-photo{left:640px;top:1272px;width:420px;height:300px}
.sec3-photo{left:170px;top:1820px;width:400px;height:420px}

/* features */
.feature-icon{width:78px;height:78px;border-radius:50%;display:flex;align-items:center;justify-content:center}
.icon-orange{background:var(--orange)}
.icon-blue{background:var(--blue)}

/* perfection */
.round-photo{left:236px;top:2888px;width:370px;height:370px;border-radius:50%;background:radial-gradient(circle at 50% 45%,#ffffff 0%,#e8ebf0 55%,#b8bec9 100%);border:10px solid var(--white)}
.round-back{left:212px;top:2870px;width:400px;height:400px;border-radius:50%;background:var(--blue-deep)}

/* banner */
.banner{left:0;top:3288px;width:1200px;height:672px;background:
  radial-gradient(ellipse at 20% 30%,rgba(230,40,120,.55),transparent 50%),
  radial-gradient(ellipse at 75% 40%,rgba(40,110,255,.6),transparent 55%),
  linear-gradient(180deg,#2a1450 0%,#1a1f5a 50%,#0c0d1e 100%)}
.banner-box{left:320px;top:3708px;width:560px;height:210px;background:var(--blue);text-align:center;padding:28px 40px}
.banner-box .heading{font-size:36px}
.banner-box p{font-size:13px;line-height:1.6;color:#e6ecff;margin-top:14px}

/* footer */
.footer{left:0;top:3960px;width:1200px;height:272px;background:var(--footer)}
.footer-links{left:0;top:4030px;width:1200px;display:flex;justify-content:center;gap:34px;font-family:"Exo 2",sans-serif;font-weight:700;font-size:15px;text-transform:uppercase;letter-spacing:.5px}
.copyright{left:0;top:4078px;width:1200px;text-align:center;font-size:12px;color:var(--muted)}
.socials{left:0;top:4138px;width:1200px;display:flex;justify-content:center;gap:26px}
.socials span{width:22px;height:22px;border-radius:50%;background:var(--white)}
</style>
</head>
<body>

<!-- hero -->
<section class="abs hero" role="img" aria-label="Sim racing gaming setup with monitors glowing in blue light"></section>
<div class="abs hero-shade"></div>
<div class="abs logo">RV MOTORSIM RIG</div>
<div class="abs lang"><i></i>EN</div>
<div class="abs menu"><span></span><span></span><span></span></div>
<h1 class="abs hero-title">Get a Sim Racing Rig</h1>
<p class="abs hero-sub">That Saves Money &amp; Performs Like an Ace</p>
<a class="abs cta">Get Started</a>
<div class="abs slide-count">01</div>
<div class="abs dots"><span></span><span></span><span></span><span></span><span></span></div>
<svg class="abs mouse" width="28" height="44" viewBox="0 0 28 44"><rect x="2" y="2" width="24" height="40" rx="12" fill="none" stroke="#fff" stroke-width="2.5"/><rect x="12.5" y="9" width="3" height="8" rx="1.5" fill="#fff"/></svg>

<!-- section 1 -->
<div class="photo-frame sec1-photo"><div class="photo photo-white" role="img" aria-label="Racer in blue suit seated in the sim racing rig"></div></div>
<div class="accent" style="left:598px;top:742px"></div>
<h2 class="abs heading" style="left:640px;top:738px;width:440px">Take Your Sim<br><span class="blue">Racing to the</span><br>Next Level</h2>
<p class="abs body-text" style="left:640px;top:880px;width:420px">The new RV Motorsim Pro Rig is all about delivering a top-notch sim racing experience. This home racing cockpit’s design is inspired with the vision to look minimal and yet offer everything that any starting up or amateur simulation racer would love to have in their rig. To serve the needs of more serious sim racing gamers, we designed the RV Motorsim Pro Rig frame around the world’s most celebrated sim racer Marek Olsvind’s own preferences. Set up your rig, install your hardware and games, sit in your seat, and lose yourself in the authentic sim racing experience delivered with a true racing posture and controls placement that pro track racers enjoy.</p>

<!-- section 2 -->
<div class="accent" style="left:120px;top:1310px"></div>
<h2 class="abs heading" style="left:140px;top:1320px;width:440px">Set Your Rig<br><span class="blue">Up to Fit Your</span><br>Needs</h2>
<p class="abs body-text" style="left:140px;top:1462px;width:440px">Meeting the needs of the modern home sim racing gamers, the RV Motorsim Pro Rig is designed to offer a lot of adjustment. Without compromising on the authentic race driving position, you can adjust most components of the rig so you can have just the kind of sim racing experience you like. This professional grade sim racing cockpit comes with adjustable settings for the seat, steering wheel, pedal plate, shifter and handbrake support, among other tweakable functions.</p>
<div class="photo-frame sec2-photo"><div class="photo photo-track" role="img" aria-label="Sim rig with blue bucket seat and steering wheel on a race track"></div></div>

<!-- section 3 -->
<div class="photo-frame sec3-photo"><div class="photo photo-white" role="img" aria-label="Player with VR headset racing in the rig"></div></div>
<div class="accent" style="left:598px;top:1902px"></div>
<h2 class="abs heading" style="left:640px;top:1898px;width:440px">Enjoy the Best<br><span class="blue">of Performance</span><br>and Pricing</h2>
<p class="abs body-text" style="left:640px;top:2040px;width:420px">The RV Motorsim Pro Rig gives you optimal performance with a commercial grade build and a simpler, compatible frame design that will conveniently turn your home into your favorite virtual race track. More than that, we have ensured you get the best product at a price few others are offering and none with the features and functions integrated into the RV Motorsim Pro Rig. With this perfect blend of performance, endurance, design, and price, you have no reason to go look for other sim racing rigs.</p>

<!-- features -->
<div class="accent" style="left:120px;top:2420px"></div>
<h2 class="abs heading" style="left:140px;top:2434px;width:440px;font-size:36px">Adjustable<br><span class="blue">Components</span></h2>
<div class="abs feature-icon icon-orange" style="left:150px;top:2570px">
  <svg width="40" height="40" viewBox="0 0 40 40"><circle cx="20" cy="20" r="7" fill="none" stroke="#fff" stroke-width="4"/><g stroke="#fff" stroke-width="5" stroke-linecap="round"><line x1="20" y1="4" x2="20" y2="9"/><line x1="20" y1="31" x2="20" y2="36"/><line x1="4" y1="20" x2="9" y2="20"/><line x1="31" y1="20" x2="36" y2="20"/><line x1="8.7" y1="8.7" x2="12" y2="12"/><line x1="28" y1="28" x2="31.3" y2="31.3"/><line x1="8.7" y1="31.3" x2="12" y2="28"/><line x1="28" y1="12" x2="31.3" y2="8.7"/></g></svg>
</div>
<p class="abs body-text" style="left:260px;top:2560px;width:320px">Set your rig components to fit your space requirements and personal posture preferences. From steering wheel position and seat-screen distance to your pedal plate and more, you can adjust every such part to get the best racing experience.</p>

<div class="accent" style="left:610px;top:2420px"></div>
<h2 class="abs heading" style="left:630px;top:2434px;width:440px;font-size:36px">A Complete<br><span class="blue">Package</span></h2>
<div class="abs feature-icon icon-blue" style="left:640px;top:2570px">
  <svg width="38" height="38" viewBox="0 0 38 38"><path d="M4 6h14l16 16-12 12L6 18z" fill="#fff"/><circle cx="12" cy="13" r="3" fill="#1d55e0"/></svg>
</div>
<p class="abs body-text" style="left:750px;top:2560px;width:320px">Your RV Motorsim Pro Rig comes as a complete package. The box contains a pre-installed base, wheel mount, side mount, wheel mount support, and seat bracket.</p>

<!-- perfection -->
<div class="abs round-back"></div>
<div class="abs round-photo" role="img" aria-label="Complete sim rig with red seat, wheel and triple monitors"></div>
<div class="accent" style="left:598px;top:3030px"></div>
<h2 class="abs heading" style="left:640px;top:3040px;width:440px">Perfection<br><span class="blue">Reimagined</span></h2>
<p class="abs body-text" style="left:640px;top:3138px;width:420px">With the RV Motorsim Pro Rig, you get the best value out of your money. At the same time, you are making sure your sim racing experience will be more fulfilling, exciting and comfortable than before.</p>

<!-- banner -->
<section class="abs banner" role="img" aria-label="Gamer room lit in pink and blue neon with racing game on screen"></section>
<div class="abs banner-box">
  <h2 class="heading">Perfection <span class="orange">Reimagined</span></h2>
  <p>We have put together the best in design, durability and performance for you. It’s time you took your sim racing passion to the next level. Feel inspired and get the rig that will give you 100% satisfaction. Order today.</p>
</div>

<!-- footer -->
<footer class="abs footer"></footer>
<nav class="abs footer-links"><span>Customer Support</span><span>/</span><span>Commercial Setups</span><span>/</span><span>FAQ</span><span>/</span><span>Dealer Resources</span><span>/</span><span>Video Instructions</span></nav>
<p class="abs copyright">© 2022 RV Motorsim Rig All Rights Reserved &nbsp;|&nbsp; Privacy Policy &nbsp;|&nbsp; Terms and Conditions</p>
<div class="abs socials"><span></span><span></span><span></span><span></span><span></span><span></span></div>

</body>
</html>
```